Design some Business Card for shipping company

We need a creative business card designed for a shipping company. All relevant information such as address and phone number can be found on our website. Will need a design for both front and back. The front will container our logo, slogan, contact information etc. The back will have a coupon and some text. check out www.talvorfreight.example for all the information. We need something memorable and unique that will stand out. It needs to a horizontal design. Not vertical.

```html
<!DOCTYPE html>
<html lang="en">
<head>
<meta charset="utf-8">
<title>Talvor Freight – Business Card</title>
<link rel="stylesheet" href="https://fonts.googleapis.com/css2?family=Quicksand:wght@500;700&family=Raleway:wght@300;500;700&display=swap">
<style>
  :root {
    --page: #e9e6e1;
    --card: #ffffff;
    --green: #2e8a4a;
    --green-dark: #1f6b36;
    --green-soft: rgba(46,138,74,.28);
    --red: #b4161f;
    --red-dark: #8e0f17;
    --red-soft: rgba(180,22,31,.22);
    --text-green: #2f7a3e;
    --shadow: rgba(0,0,0,.18);
  }
  * { box-sizing: border-box; margin: 0; padding: 0; }
  html, body { width: 1200px; height: 912px; overflow: hidden; }
  body { background: var(--page); position: relative; font-family: "Quicksand", sans-serif; }

  .card {
    position: absolute; width: 640px; height: 366px;
    background: var(--card); border-radius: 22px; overflow: hidden;
    box-shadow: 0 10px 28px var(--shadow);
  }
  .card--back { left: 80px; top: 70px; }
  .card--front { left: 480px; top: 476px; }

  /* soft decorative areas */
  .ribbon-area { position: absolute; pointer-events: none; }
  .ribbon-area--corner-right {
    right: 0; top: 0; width: 220px; height: 240px;
    background: radial-gradient(ellipse 100% 100% at 100% 0%, var(--green-soft) 0%, var(--red-soft) 45%, rgba(255,255,255,0) 75%);
  }
  .ribbon-area--edge-left {
    left: 0; top: 70px; width: 110px; height: 230px;
    background: radial-gradient(ellipse 100% 60% at 0% 50%, var(--green-soft) 0%, var(--red-soft) 40%, rgba(255,255,255,0) 75%);
  }
  .ribbon-area--front-left {
    left: 0; top: 0; width: 120px; height: 230px;
    background: radial-gradient(ellipse 100% 70% at 0% 30%, var(--green-soft) 0%, var(--red-soft) 40%, rgba(255,255,255,0) 75%);
  }
  .travel-icon {
    position: absolute; border-radius: 50%;
    background: radial-gradient(circle, rgba(46,138,74,.45) 0%, rgba(46,138,74,0) 70%);
  }

  /* brand */
  .brand { display: flex; align-items: center; gap: 10px; }
  .brand__dot { width: 22px; height: 22px; border-radius: 50%; background: var(--red); flex: none; }
  .brand__name { font-weight: 700; color: var(--green-dark); letter-spacing: .5px; }
  .brand__slogan { font-weight: 700; color: var(--green-dark); }

  /* back */
  .back__brand { position: absolute; left: 0; right: 0; top: 70px; display: flex; flex-direction: column; align-items: center; gap: 2px; }
  .back__brand .brand__name { font-size: 20px; }
  .back__brand .brand__slogan { font-size: 10px; }
  .back__copy {
    position: absolute; left: 90px; right: 90px; top: 140px;
    font-size: 15px; line-height: 1.55; font-weight: 500; color: var(--text-green);
  }
  .back__copy strong { font-weight: 700; }

  /* front */
  .front__brand { position: absolute; left: 150px; top: 62px; display: flex; flex-direction: column; gap: 4px; }
  .front__brand .brand__name { font-size: 30px; }
  .front__brand .brand__slogan { font-size: 14px; padding-left: 32px; }

  .front__name-band {
    position: absolute; left: 0; bottom: 0; width: 352px; height: 150px;
    background: linear-gradient(180deg, var(--red) 0%, var(--red-dark) 100%);
    padding: 34px 0 0 70px; color: #fff;
  }
  .person__name { font-family: "Raleway", sans-serif; font-weight: 300; font-size: 28px; }
  .person__name b { font-weight: 500; }
  .person__role { font-family: "Raleway", sans-serif; font-weight: 700; font-size: 11px; letter-spacing: 1px; margin-top: 2px; }

  .front__contact-band {
    position: absolute; right: 0; bottom: 0; width: 288px; height: 196px;
    background: linear-gradient(180deg, var(--green) 0%, var(--green-dark) 100%);
    padding: 26px 16px 0 24px; color: #fff;
    font-family: "Raleway", sans-serif; font-size: 12px; font-weight: 500;
  }
  .contact { list-style: none; display: grid; gap: 9px; }
  .contact__row { display: grid; grid-template-columns: 18px 56px 1fr; align-items: center; column-gap: 8px; }
  .contact__row--wide { grid-template-columns: 18px 1fr; }
  .contact__icon { width: 14px; height: 14px; }
</style>
</head>
<body>

<section class="card card--back" aria-label="Card back">
  <div class="ribbon-area ribbon-area--corner-right" role="img" aria-label="Curved green, red and black ribbon decoration"></div>
  <div class="ribbon-area ribbon-area--edge-left" role="img" aria-label="Curved green and red ribbon decoration"></div>
  <div class="travel-icon" role="img" aria-label="Airplane icon" style="left:14px;top:136px;width:54px;height:54px;"></div>
  <div class="travel-icon" role="img" aria-label="Cargo ship icon" style="right:22px;top:190px;width:60px;height:60px;"></div>

  <div class="back__brand">
    <div class="brand"><span class="brand__dot"></span><span class="brand__name">Talvor Freight</span></div>
    <div class="brand__slogan">Secure Affordable Shipping to Kenya</div>
  </div>
  <p class="back__copy"><strong>Fast, secure and reliable ocean shipping service to Kenya from the USA.</strong> Our rates include customs and duty all the way to our warehouse in Nairobi. Packages are picked up from our Mombasa road warehouse. Door to door delivery also available. All prices are based on volume. Weight does not matter. Free package pick up in the Seattle area.</p>
</section>

<section class="card card--front" aria-label="Card front">
  <div class="ribbon-area ribbon-area--front-left" role="img" aria-label="Curved green and red ribbon decoration"></div>
  <div class="travel-icon" role="img" aria-label="Airplane icon" style="left:16px;top:50px;width:54px;height:54px;"></div>

  <div class="front__brand">
    <div class="brand"><span class="brand__dot"></span><span class="brand__name">Talvor Freight</span></div>
    <div class="brand__slogan">Secure Affordable Shipping to Kenya</div>
  </div>

  <div class="front__name-band">
    <div class="person__name">Dana <b>REYES</b></div>
    <div class="person__role">PROJECT MANAGER</div>
  </div>

  <div class="front__contact-band">
    <ul class="contact">
      <li class="contact__row">
        <svg class="contact__icon" viewBox="0 0 24 24" aria-hidden="true"><path fill="#fff" d="M6.6 10.8a15 15 0 0 0 6.6 6.6l2.2-2.2c.3-.3.7-.4 1-.2 1.1.4 2.3.6 3.6.6.6 0 1 .4 1 1V20c0 .6-.4 1-1 1A17 17 0 0 1 3 4c0-.6.4-1 1-1h3.5c.6 0 1 .4 1 1 0 1.3.2 2.5.6 3.6.1.3 0 .7-.2 1z"/></svg>
        <span>USA</span><span>+1 555 014 2290</span>
      </li>
      <li class="contact__row">
        <svg class="contact__icon" viewBox="0 0 24 24" aria-hidden="true"><path fill="#fff" d="M6.6 10.8a15 15 0 0 0 6.6 6.6l2.2-2.2c.3-.3.7-.4 1-.2 1.1.4 2.3.6 3.6.6.6 0 1 .4 1 1V20c0 .6-.4 1-1 1A17 17 0 0 1 3 4c0-.6.4-1 1-1h3.5c.6 0 1 .4 1 1 0 1.3.2 2.5.6 3.6.1.3 0 .7-.2 1z"/></svg>
        <span>Kenya</span><span>+254 700 000 481</span>
      </li>
      <li class="contact__row contact__row--wide">
        <svg class="contact__icon" viewBox="0 0 24 24" aria-hidden="true"><rect x="2" y="5" width="20" height="14" rx="2" fill="#fff"/><path d="M3 6l9 7 9-7" fill="none" stroke="var(--green)" stroke-width="2"/></svg>
        <span>mail@talvorfreight.example</span>
      </li>
      <li class="contact__row contact__row--wide">
        <svg class="contact__icon" viewBox="0 0 24 24" aria-hidden="true"><circle cx="12" cy="12" r="9" fill="none" stroke="#fff" stroke-width="2"/><path d="M3 12h18M12 3c3 3 3 15 0 18M12 3c-3 3-3 15 0 18" fill="none" stroke="#fff" stroke-width="1.6"/></svg>
        <span>www.talvorfreight.example</span>
      </li>
    </ul>
  </div>
</section>

</body>
</html>
```